Bref créative
Celvoria Brochure
12 pages brochure
It's a 12 pages brochure about a molecular laboratory.
High tech project innovator and at the same time very reliable
Health
Doctors
Advanced concept but at the same time show professionalism
Attached is a brochure that was initiated but not finished by another designer.
cytovane logo

```html
<!DOCTYPE html>
<html lang="en">
<head>
<meta charset="utf-8">
<title>Celvoria Brochure Spread</title>
<link rel="stylesheet" href="https://fonts.googleapis.com/css2?family=Open+Sans:wght@300;400;600&display=swap">
<style>
  :root {
    --page: #ffffff;
    --ink: #66696d;
    --heading-blue: #3e9fd6;
    --menu-blue: #2f8fcf;
    --brand-green: #3c8a5c;
    --deep-navy: #04101f;
    --screen-blue: #0f4f8c;
    --lab-light: #dbe7f1;
    --lab-blue: #5d8fbf;
    --band-red: #d8262e;
    --band-orange: #ef7d1a;
    --band-yellow: #f2c21b;
    --band-lime: #9cc63b;
    --band-green: #3ca650;
    --band-teal: #1aa0a8;
    --band-blue: #2b73c2;
  }
  * { margin: 0; padding: 0; box-sizing: border-box; }
  html, body { width: 1200px; height: 780px; overflow: hidden; background: var(--page); }
  .spread {
    position: relative; width: 1200px; height: 780px; background: var(--page);
    font-family: "Open Sans", Arial, sans-serif; color: var(--ink);
  }
  .dna-visual {
    position: absolute; left: 0; top: 0; width: 585px; height: 378px;
    background: radial-gradient(ellipse at 40% 45%, var(--screen-blue) 0%, #082a52 45%, var(--deep-navy) 85%);
  }
  .pcr-menu { position: absolute; left: 230px; top: 476px; }
  .section-title {
    font-weight: 300; font-size: 19px; letter-spacing: 0.3px; color: var(--menu-blue);
    text-transform: uppercase; line-height: 1.2; white-space: nowrap;
  }
  .item-list { list-style: none; margin-top: 12px; }
  .item-list li { font-size: 11.5px; line-height: 19px; text-transform: uppercase; color: var(--ink); white-space: nowrap; }
  .portfolio { position: absolute; left: 230px; top: 636px; }
  .portfolio .item-list { margin-top: 8px; }
  .portfolio .item-list li { font-size: 13px; line-height: 18px; }
  .brand {
    position: absolute; left: 50px; top: 664px; display: flex; align-items: center; gap: 8px;
  }
  .brand-dot { width: 14px; height: 14px; border-radius: 50%; background: var(--brand-green); }
  .brand-name { font-weight: 600; font-size: 22px; color: var(--brand-green); }
  .intro { position: absolute; left: 744px; top: 136px; width: 330px; }
  .intro-title { font-weight: 300; font-size: 22px; line-height: 25px; color: var(--heading-blue); }
  .intro-body {
    margin-top: 10px; font-size: 11.3px; line-height: 16px; color: var(--ink);
    text-align: justify;
  }
  .lab-photo {
    position: absolute; left: 744px; top: 410px; width: 330px; height: 336px;
    background: linear-gradient(135deg, var(--lab-light) 0%, #a9c6e0 45%, var(--lab-blue) 100%);
  }
  .color-band { position: absolute; left: 0; bottom: 0; width: 1200px; height: 12px; display: flex; }
  .color-band span { flex: 1; }
</style>
</head>
<body>
<div class="spread">
  <div class="dna-visual" role="img" aria-label="Glowing blue DNA sequence letters on a dark digital screen"></div>

  <section class="pcr-menu">
    <h2 class="section-title">Top molecular PCR menu</h2>
    <ul class="item-list">
      <li>Lung cancer</li>
      <li>Colorectal cancer</li>
      <li>Gastric cancer</li>
      <li>Melanoma</li>
      <li>Brain tumor</li>
      <li>Other</li>
    </ul>
  </section>

  <section class="portfolio">
    <h2 class="section-title">Celvoria molecular portfolio</h2>
    <ul class="item-list">
      <li>CV-ID-Card</li>
      <li>Celvoria Earlyscan</li>
      <li>Genetic diseases-inherited mutations</li>
    </ul>
  </section>

  <div class="brand">
    <span class="brand-dot"></span>
    <span class="brand-name">Celvoria</span>
  </div>

  <section class="intro">
    <h1 class="intro-title">Genetic diseases diagnostic and inherited mutations analysis</h1>
    <p class="intro-body">Celvoria offers next-generation sequencing technologies to analyze more than 300 genes and 10,000 amplicons implicated in several diseases, like deafness, cardiovascular diseases, inborn errors of metabolism, neuromuscular diseases, retinitis pigmentosa, Parkinson syndrome, Charcot Marie Tooth disease, mental retardation, etc. Our genetic testing are reported by licensed and certified health professionals. They gather relevant data and interpret it for patients, providing in-depth support, and facilitating thoroughly informed, autonomous decisions.</p>
  </section>

  <div class="lab-photo" role="img" aria-label="Laboratory scientist in protective cap and mask working at a microscope"></div>

  <div class="color-band">
    <span style="background: var(--band-red)"></span>
    <span style="background: var(--band-orange)"></span>
    <span style="background: var(--band-yellow)"></span>
    <span style="background: var(--band-lime)"></span>
    <span style="background: var(--band-green)"></span>
    <span style="background: var(--band-teal)"></span>
    <span style="background: var(--band-blue)"></span>
    <span style="background: var(--band-red)"></span>
  </div>
</div>
</body>
</html>
```